Proposal Template Design

We are looking to have our proposal templates redesigned. attached are examples of what we have been using. as well as our current logo

```html
<!DOCTYPE html>
<html lang="en">
<head>
<meta charset="utf-8">
<title>Northline Spray Foam – Proposal Template</title>
<link href="https://fonts.googleapis.com/css2?family=Montserrat:ital,wght@0,400;0,500;0,600;0,700;0,800;1,800&display=swap" rel="stylesheet">
<style>
  :root{
    --bg:#c5c7c6;
    --paper:#ffffff;
    --sky:#1ea7e1;
    --royal:#0d4d8c;
    --navy:#062d55;
    --mid:#2f6fb1;
    --ink:#3d3d3d;
    --grey:#c6c6c6;
    --grey-dark:#9c9c9c;
    --charcoal:#262626;
  }
  *{box-sizing:border-box;margin:0;padding:0}
  html,body{width:1200px;height:1018px;overflow:hidden;background:var(--bg)}
  body{position:relative;font-family:'Montserrat',sans-serif;color:var(--ink)}
  .page{position:absolute;width:336px;height:435px;background:var(--paper);overflow:hidden;box-shadow:0 1px 3px rgba(0,0,0,.15)}
  .page > svg.deco{position:absolute;left:0;top:0;width:336px;height:435px}
  .p1{left:77px;top:66px}.p2{left:430px;top:66px}.p3{left:786px;top:66px}
  .p4{left:77px;top:516px}.p5{left:430px;top:516px}.p6{left:786px;top:516px}
  .abs{position:absolute}
  .brand{position:absolute;left:24px;top:33px;color:var(--royal);font-weight:800;font-size:6.2px;line-height:1.05;width:60px}
  .running-head{position:absolute;right:21px;top:27px;color:var(--royal);font-weight:800;font-style:italic;font-size:8.5px;letter-spacing:.4px}
  .folio{position:absolute;left:310px;top:413px;color:#fff;font-size:5px;font-weight:600}
  .h{color:var(--royal);font-weight:700;font-size:11px;letter-spacing:.2px}
  .h-sm{color:var(--royal);font-weight:700;font-size:8px}
  .body{font-size:6.6px;line-height:8px;color:var(--ink)}
  .body-sm{font-size:5.4px;line-height:6.6px;color:var(--ink)}
  .bullets{list-style:none;font-size:6.6px;line-height:8px}
  .bullets li::before{content:"";display:inline-block;width:6px;height:2px;background:var(--royal);margin-right:4px;vertical-align:middle;clip-path:polygon(0 50%,100% 0,100% 100%)}
  /* cover */
  .cover-brand{position:absolute;left:26px;top:40px;color:var(--royal);font-weight:800;font-size:12px;line-height:1.05;width:100px}
  .cover-services{position:absolute;left:229px;top:66px;list-style:none;font-size:8px;font-weight:600;color:var(--navy);line-height:10.4px}
  .cover-services li::before{content:"";display:inline-block;width:9px;height:3px;background:var(--navy);margin-right:3px;vertical-align:middle;clip-path:polygon(0 50%,100% 0,100% 100%)}
  .cover-title{position:absolute;left:28px;top:113px;width:280px;color:var(--sky);font-weight:800;font-style:italic;font-size:22.5px;line-height:22px;letter-spacing:.5px;text-align:center}
  /* numbered list */
  .num-item{position:absolute;left:44px;width:260px;display:flex;gap:10px}
  .num-item span:first-child{width:7px}
  .callout{position:absolute;width:48px;height:12px;border-radius:2px;font-size:3.6px;line-height:4.2px;color:#fff;display:flex;align-items:center;justify-content:center;text-align:center}
  .callout.blue{background:var(--sky)}
  .callout.grey{background:var(--grey-dark);color:#333}
  .hub-label{position:absolute;left:47px;top:324px;width:72px;text-align:center;color:#fff;font-weight:700;font-size:6.2px;line-height:7.5px}
  /* table */
  .tbl-title{position:absolute;left:0;width:336px;top:223px;text-align:center;color:var(--royal);font-weight:700;font-size:10.5px}
  .cell{position:absolute;font-size:4.6px;color:#333;text-align:center}
  .cell.head{color:#fff;font-weight:700;font-size:5.2px}
  .row-label{position:absolute;left:31px;font-size:4.8px;color:#333}
  /* back cover */
  .back-brand{position:absolute;left:0;width:336px;top:162px;text-align:center;color:var(--royal);font-weight:800;font-size:15px;line-height:17px}
  .contact{position:absolute;left:93px;list-style:none;font-size:7.6px;font-weight:600;color:var(--charcoal)}
  .contact li{display:flex;align-items:center;gap:5px;height:17px}
  .contact svg{width:9px;height:9px}
</style>
</head>
<body>

<!-- Page 1: cover -->
<section class="page p1">
  <svg class="deco" viewBox="0 0 583 754" aria-hidden="true">
    <path d="M0,0H130C115,30 85,45 55,46C30,46 10,40 0,35Z" fill="var(--sky)"/>
    <path d="M350,0H415C360,25 320,90 270,135C230,170 180,182 130,180C80,178 30,165 0,145L0,141C40,160 100,170 160,165C230,158 270,110 300,60C320,30 335,10 350,0Z" fill="var(--royal)"/>
    <path d="M583,560C520,560 470,590 430,640C410,665 395,700 385,754H583Z" fill="var(--royal)"/>
    <path d="M0,600C60,560 110,640 180,690C240,720 290,640 340,600C400,555 480,560 583,585L583,754L0,754Z" fill="var(--sky)"/>
    <path d="M390,754C420,690 480,640 583,615L583,754Z" fill="var(--royal)"/>
    <path d="M420,754C450,700 510,665 583,650L583,754Z" fill="var(--navy)"/>
    <path d="M0,690C20,720 40,740 55,754L0,754Z" fill="var(--navy)"/>
  </svg>
  <svg class="deco" viewBox="0 0 583 754" role="img" aria-label="Photo of a worker spraying foam insulation onto wall studs, blue toned">
    <defs><linearGradient id="photoTone" x1="0" y1="0" x2="1" y2="1"><stop offset="0" stop-color="#4f7fc4"/><stop offset=".55" stop-color="#8fb5e6"/><stop offset="1" stop-color="#2f5ea6"/></linearGradient></defs>
    <path d="M0,370C40,345 80,345 105,332C100,300 125,285 150,292C180,280 220,292 240,318C270,305 300,318 310,330C340,318 380,330 385,355C410,368 405,410 395,432C420,452 430,490 420,512C440,540 480,560 505,565C440,600 380,680 330,715C250,720 200,700 180,690C110,640 60,560 0,600Z" fill="url(#photoTone)"/>
  </svg>
  <div class="cover-brand">Northline<br>Spray Foam</div>
  <ul class="cover-services">
    <li>SPRAY FOAM</li><li>FIBERGLASS</li><li>INSULATION</li><li>ROOFING</li>
  </ul>
  <h1 class="cover-title">NORTHLINE<br>SPRAY FOAM</h1>
</section>

<!-- Page 2 -->
<section class="page p2">
  <svg class="deco" viewBox="0 0 583 754" aria-hidden="true">
    <path d="M0,0H80C70,20 50,30 30,30C15,30 5,25 0,20Z" fill="var(--sky)"/>
    <path d="M215,0H275C235,30 215,80 175,105C135,128 60,130 0,110L0,107C60,125 130,118 165,90C195,65 195,20 215,0Z" fill="var(--royal)"/>
    <line x1="210" y1="57" x2="402" y2="57" stroke="var(--royal)" stroke-width="1"/>
    <path d="M583,590L583,754L420,754C470,680 520,630 583,590Z" fill="var(--navy)"/>
    <path d="M0,680L0,754L48,754C30,735 12,710 0,680Z" fill="var(--navy)"/>
  </svg>
  <div class="brand">Northline<br>Spray Foam</div>
  <div class="running-head">LOREM IPSUM</div>
  <h2 class="h abs" style="left:25px;top:110px">HEADING ONE</h2>
  <p class="body abs" style="left:26px;top:128px;width:284px">Lorem Ipsum is simply dummy text of the printing and typesetting industry. Lorem Ipsum has been the industry's standard dummy text ever since the 1500s, when an unknown printer took a galley of type and scrambled it to make a type specimen book. It has survived not only five centuries, but also the leap into electronic typesetting, remaining essentially unchanged. It was popularised in the 1960s with the release of Letraset sheets containing Lorem Ipsum passages, and more recently with desktop publishing software like Aldus PageMaker including versions of Lorem Ipsum.</p>
  <h2 class="h abs" style="left:25px;top:204px">HEADING TWO</h2>
  <p class="body abs" style="left:26px;top:221px;width:284px">Lorem Ipsum is simply dummy text of the printing and typesetting industry. Lorem Ipsum has been the industry's standard dummy text ever since the 1500s, when an unknown printer took a galley of type and scrambled it to make a type specimen book.</p>
  <h2 class="h abs" style="left:25px;top:279px">HEADING THREE</h2>
  <ul class="bullets abs" style="left:26px;top:295px">
    <li>Lorem Ipsum</li><li>Lorem Ipsum is simply dummy</li><li>Lorem Ipsum is</li><li>Lorem Ipsum is simply</li>
  </ul>
  <span class="folio">2</span>
</section>

<!-- Page 3 -->
<section class="page p3">
  <svg class="deco" viewBox="0 0 583 754" aria-hidden="true">
    <path d="M0,0H80C70,20 50,30 30,30C15,30 5,25 0,20Z" fill="var(--sky)"/>
    <path d="M215,0H275C235,30 215,80 175,105C135,128 60,130 0,110L0,107C60,125 130,118 165,90C195,65 195,20 215,0Z" fill="var(--royal)"/>
    <line x1="210" y1="57" x2="402" y2="57" stroke="var(--royal)" stroke-width="1"/>
    <path d="M583,590L583,754L420,754C470,680 520,630 583,590Z" fill="var(--navy)"/>
    <path d="M0,680L0,754L48,754C30,735 12,710 0,680Z" fill="var(--navy)"/>
  </svg>
  <div class="brand">Northline<br>Spray Foam</div>
  <div class="running-head">LOREM IPSUM</div>
  <h2 class="h abs" style="left:25px;top:86px">OUR SERVICES</h2>
  <h3 class="h-sm abs" style="left:26px;top:112px">1. SPRAY FOAM INSULATION</h3>
  <p class="body-sm abs" style="left:27px;top:125px;width:282px">Lorem Ipsum is simply dummy text of the printing and typesetting industry. Lorem Ipsum has been the industry's standard dummy text ever since the 1500s, when an unknown printer took a galley of type and scrambled it to make a type specimen book. It has survived not only five centuries, but also the leap into electronic typesetting, remaining essentially unchanged. It was popularised in the 1960s with the release of Letraset sheets containing Lorem Ipsum passages, and more recently with desktop publishing software like Aldus PageMaker including versions of Lorem Ipsum.</p>
  <h3 class="h-sm abs" style="left:26px;top:178px">2. FIBER GLASS INSULATION</h3>
  <p class="body-sm abs" style="left:26px;top:191px;width:282px">Lorem Ipsum is simply dummy text of the printing and typesetting industry. Lorem Ipsum has been the industry's standard dummy text ever since the 1500s, when an unknown printer took a galley of type and scrambled it to make a type specimen book. It has survived not only five centuries, but also the leap into electronic typesetting, remaining essentially unchanged. It was popularised in the 1960s with the release of Letraset sheets containing Lorem Ipsum passages, and more recently with desktop publishing software like Aldus PageMaker including versions of Lorem Ipsum.</p>
  <h3 class="h-sm abs" style="left:26px;top:241px">3. AIR SEALING</h3>
  <p class="body-sm abs" style="left:26px;top:254px;width:282px">Lorem Ipsum is simply dummy text of the printing and typesetting industry. Lorem Ipsum has been the industry's standard dummy text ever since the 1500s, when an unknown printer took a galley of type and scrambled it to make a type specimen book.</p>
  <h3 class="h-sm abs" style="left:26px;top:282px">4. INSULATION REMOVAL</h3>
  <p class="body-sm abs" style="left:26px;top:295px;width:292px">Lorem Ipsum is simply dummy text of the printing and typesetting industry. Lorem Ipsum has been the industry's standard dummy text ever since the 1500s, when an unknown printer took a galley of type and scrambled it to make a type specimen book. It has survived not only five centuries, but also the leap into electronic typesetting, remaining essentially unchanged. It was popularised in the 1960s with the release of Letraset sheets containing Lorem Ipsum passages, and more recently with desktop publishing software like Aldus PageMaker including versions of Lorem Ipsum.</p>
  <h3 class="h-sm abs" style="left:26px;top:345px">5. ATTIC VENTILATION</h3>
  <p class="body-sm abs" style="left:26px;top:358px;width:236px">Lorem Ipsum is simply dummy text of the printing and typesetting industry. Lorem Ipsum has been the industry's standard dummy text ever since the 1500s, when an unknown printer took a galley of type and scrambled it to make a type specimen book. It has survived not only five centuries, but also the leap into electronic typesetting, remaining essentially unchanged. It was popularised in the 1960s with the release of Letraset sheets containing Lorem Ipsum passages, and more recently with desktop publishing software like Aldus PageMaker including versions of Lorem Ipsum.</p>
  <span class="folio">3</span>
</section>

<!-- Page 4 -->
<section class="page p4">
  <svg class="deco" viewBox="0 0 583 754" aria-hidden="true">
    <path d="M0,0H80C70,20 50,30 30,30C15,30 5,25 0,20Z" fill="var(--sky)"/>
    <path d="M215,0H275C235,30 215,80 175,105C135,128 60,130 0,110L0,107C60,125 130,118 165,90C195,65 195,20 215,0Z" fill="var(--royal)"/>
    <line x1="210" y1="57" x2="402" y2="57" stroke="var(--royal)" stroke-width="1"/>
    <path d="M583,590L583,754L420,754C470,680 520,630 583,590Z" fill="var(--navy)"/>
    <path d="M0,680L0,754L48,754C30,735 12,710 0,680Z" fill="var(--navy)"/>
    <g stroke="#fff" stroke-width="2">
      <path d="M144,458A120,120 0 0 1 214.6,480.9L182.8,524.6A54,54 0 0 0 144,512Z" fill="var(--sky)"/>
      <path d="M214.6,480.9A120,120 0 0 1 258.1,540.9L206.8,557.6A54,54 0 0 0 182.8,524.6Z" fill="var(--royal)"/>
      <path d="M258.1,540.9A120,120 0 0 1 258.1,615.1L206.8,598.4A54,54 0 0 0 206.8,557.6Z" fill="var(--royal)"/>
      <path d="M258.1,615.1A120,120 0 0 1 214.6,675.1L182.8,631.4A54,54 0 0 0 206.8,598.4Z" fill="var(--mid)"/>
      <path d="M214.6,675.1A120,120 0 0 1 144,698L144,644A54,54 0 0 0 182.8,631.4Z" fill="var(--royal)"/>
    </g>
    <circle cx="144" cy="578" r="66" fill="var(--charcoal)" stroke="#fff" stroke-width="3"/>
    <g stroke="#555" stroke-width="1" stroke-dasharray="3 2" fill="none">
      <line x1="190" y1="466" x2="292" y2="466"/>
      <line x1="255" y1="522" x2="345" y2="522"/>
      <line x1="270" y1="579" x2="372" y2="579"/>
      <line x1="255" y1="636" x2="347" y2="636"/>
      <line x1="190" y1="692" x2="288" y2="692"/>
    </g>
  </svg>
  <div class="brand">Northline<br>Spray Foam</div>
  <div class="running-head">LOREM IPSUM</div>
  <h2 class="h abs" style="left:25px;top:91px">1. HEADING ONE</h2>
  <p class="body-sm abs" style="left:26px;top:110px;width:282px;font-size:5.6px;line-height:6.6px">Lorem Ipsum is simply dummy text of the printing and typesetting industry. Lorem Ipsum has been the industry's standard dummy text ever since the 1500s, when an unknown printer took a galley of type and scrambled it to make a type specimen book. It has survived not only five centuries, but also the leap into electronic typesetting, remaining essentially unchanged. It was popularised in the 1960s with the release of Letraset sheets containing Lorem Ipsum passages, and more recently with desktop publishing software like Aldus PageMaker including versions of Lorem Ipsum.</p>
  <h3 class="h-sm abs" style="left:43px;top:159px;font-size:8.6px">1.1 HEADING TWO</h3>
  <div class="num-item body-sm" style="top:175px"><span>1.1</span><span>Lorem Ipsum is simply dummy text of the printing and typesetting industry. Lorem Ipsum has been the industry's standard dummy text ever since the 1500s, when an unknown printer took a galley of type and scrambled it to make a type specimen book.</span></div>
  <div class="num-item body-sm" style="top:204px"><span>1.2</span><span>Lorem Ipsum is simply dummy text of the printing and typesetting industry. Lorem Ipsum has been the industry's standard dummy text ever since the 1500s, when an unknown printer took a galley of type and scrambled it to make a type specimen book.</span></div>
  <div class="num-item body-sm" style="top:233px"><span>1.3</span><span>Lorem Ipsum is simply dummy text of the printing and typesetting industry. Lorem Ipsum has been the industry's standard dummy text ever since the 1500s, when an unknown printer took a galley of type and scrambled it to make a type specimen book.</span></div>
  <div class="hub-label">LOREM IPSUM<br>IS SIMPLY</div>
  <div class="callout blue" style="left:172px;top:262px">Lorem Ipsum</div>
  <div class="callout grey" style="left:204px;top:295px">Lorem Ipsum is simply dummy</div>
  <div class="callout blue" style="left:219px;top:328px">Lorem Ipsum is simply dummy</div>
  <div class="callout grey" style="left:205px;top:361px">Lorem Ipsum is simply dummy</div>
  <div class="callout blue" style="left:170px;top:393px">Lorem Ipsum is simply</div>
  <span class="folio">4</span>
</section>

<!-- Page 5 -->
<section class="page p5">
  <svg class="deco" viewBox="0 0 583 754" aria-hidden="true">
    <path d="M0,0H80C70,20 50,30 30,30C15,30 5,25 0,20Z" fill="var(--sky)"/>
    <path d="M215,0H275C235,30 215,80 175,105C135,128 60,130 0,110L0,107C60,125 130,118 165,90C195,65 195,20 215,0Z" fill="var(--royal)"/>
    <line x1="210" y1="57" x2="402" y2="57" stroke="var(--royal)" stroke-width="1"/>
    <path d="M583,590L583,754L420,754C470,680 520,630 583,590Z" fill="var(--navy)"/>
    <path d="M0,680L0,754L48,754C30,735 12,710 0,680Z" fill="var(--navy)"/>
    <g fill="var(--royal)">
      <rect x="127" y="425" width="90" height="27"/><rect x="219" y="425" width="85" height="27"/>
      <rect x="307" y="425" width="85" height="27"/><rect x="394" y="425" width="85" height="27"/>
    </g>
    <g fill="var(--sky)">
      <rect x="127" y="457" width="90" height="28"/><rect x="219" y="457" width="85" height="28"/>
      <rect x="307" y="457" width="85" height="28"/><rect x="394" y="457" width="85" height="28"/>
      <rect x="127" y="553" width="90" height="29"/><rect x="219" y="553" width="85" height="29"/>
      <rect x="307" y="553" width="85" height="29"/><rect x="394" y="553" width="85" height="29"/>
    </g>
    <g fill="var(--grey)">
      <rect x="127" y="488" width="90" height="27"/><rect x="219" y="488" width="85" height="27"/>
      <rect x="307" y="488" width="85" height="27"/><rect x="394" y="488" width="85" height="27"/>
      <rect x="127" y="585" width="90" height="27"/><rect x="219" y="585" width="85" height="27"/>
      <rect x="307" y="585" width="85" height="27"/><rect x="394" y="585" width="85" height="27"/>
    </g>
    <g fill="var(--grey-dark)">
      <rect x="127" y="520" width="90" height="28"/><rect x="219" y="520" width="85" height="28"/>
      <rect x="307" y="520" width="85" height="28"/><rect x="394" y="520" width="85" height="28"/>
      <rect x="127" y="617" width="90" height="28"/><rect x="219" y="617" width="85" height="28"/>
      <rect x="307" y="617" width="85" height="28"/><rect x="394" y="617" width="85" height="28"/>
    </g>
    <g stroke="#555" stroke-width="1">
      <line x1="56" y1="452" x2="479" y2="452"/><line x1="56" y1="517" x2="479" y2="517"/>
      <line x1="56" y1="550" x2="479" y2="550"/><line x1="56" y1="614" x2="479" y2="614"/>
      <line x1="56" y1="647" x2="479" y2="647"/>
    </g>
  </svg>
  <div class="brand">Northline<br>Spray Foam</div>
  <div class="running-head">LOREM IPSUM</div>
  <h2 class="h abs" style="left:26px;top:83px">WHY CHOOSE US</h2>
  <p class="body-sm abs" style="left:26px;top:105px;width:264px">Lorem Ipsum is simply dummy text of the printing and typesetting industry. Lorem Ipsum has been the industry's standard dummy text ever since the 1500s, when an unknown printer took a galley of type and scrambled it to make a type specimen book. It has survived not only five centuries, but also the leap into electronic typesetting, remaining essentially unchanged. It was popularised in the 1960s with the release of Letraset sheets containing Lorem Ipsum passages, and more recently with desktop publishing software like Aldus PageMaker including versions of Lorem Ipsum.</p>
  <p class="body-sm abs" style="left:26px;top:159px;width:264px">Lorem Ipsum is simply dummy text of the printing and typesetting industry. Lorem Ipsum has been the industry's standard dummy text ever since the 1500s, when an unknown printer took a galley of type and scrambled it to make a type specimen book. It has survived not only five centuries, but also the leap into electronic typesetting, remaining essentially unchanged. It was popularised in the 1960s with the release of Letraset sheets containing Lorem Ipsum passages, and more recently with desktop publishing software like Aldus PageMaker including versions of Lorem Ipsum.</p>
  <div class="tbl-title">Lorem Ipsum</div>
  <div class="cell head" style="left:73px;width:52px;top:248px">LOREM IPSUM</div>
  <div class="cell head" style="left:126px;width:49px;top:248px">LOREM IPSUM</div>
  <div class="cell head" style="left:177px;width:49px;top:248px">LOREM IPSUM</div>
  <div class="cell head" style="left:227px;width:49px;top:248px">LOREM IPSUM</div>
  <div class="row-label" style="top:280px">Lorem Ipsum</div>
  <div class="row-label" style="top:308px">Lorem Ipsum</div>
  <div class="row-label" style="top:336px">Lorem Ipsum</div>
  <div class="row-label" style="top:364px">Lorem Ipsum</div>
  <div class="cell" style="left:73px;width:52px;top:267px">Lorem Ipsum</div>
  <div class="cell" style="left:177px;width:49px;top:267px">Lorem Ipsum</div>
  <div class="cell" style="left:126px;width:49px;top:285px">Lorem Ipsum</div>
  <div class="cell" style="left:227px;width:49px;top:285px">Lorem Ipsum</div>
  <div class="cell" style="left:73px;width:52px;top:304px">Lorem Ipsum</div>
  <div class="cell" style="left:126px;width:49px;top:304px">Lorem Ipsum</div>
  <div class="cell" style="left:177px;width:49px;top:304px">Lorem Ipsum</div>
  <div class="cell" style="left:73px;width:52px;top:324px">Lorem Ipsum</div>
  <div class="cell" style="left:126px;width:49px;top:324px">Lorem Ipsum</div>
  <div class="cell" style="left:177px;width:49px;top:324px">Lorem Ipsum</div>
  <div class="cell" style="left:227px;width:49px;top:324px">Lorem Ipsum</div>
  <div class="cell" style="left:126px;width:49px;top:361px">Lorem Ipsum</div>
  <span class="folio">5</span>
</section>

<!-- Page 6: back cover -->
<section class="page p6">
  <svg class="deco" viewBox="0 0 583 754" aria-hidden="true">
    <path d="M583,560C530,555 490,570 455,585L583,620Z" fill="var(--royal)"/>
    <path d="M0,585C30,560 60,600 80,640C110,700 170,705 235,665C305,620 360,565 460,575C520,582 560,600 583,615L583,754L0,754Z" fill="var(--sky)"/>
    <path d="M390,754C425,695 490,650 583,635L583,754Z" fill="var(--royal)"/>
    <path d="M425,754C455,705 515,675 583,665L583,754Z" fill="var(--navy)"/>
    <g fill="var(--charcoal)">
      <circle cx="356" cy="590" r="11"/><circle cx="389" cy="590" r="11"/><circle cx="421" cy="590" r="11"/>
    </g>
  </svg>
  <div class="back-brand">Northline<br>Spray Foam</div>
  <ul class="contact" style="top:234px">
    <li><svg viewBox="0 0 10 10" aria-hidden="true"><circle cx="5" cy="5" r="5" fill="var(--royal)"/><path d="M5,2.2a1.6,1.6 0 0 1 1.6,1.6C6.6,5 5,7.4 5,7.4S3.4,5 3.4,3.8A1.6,1.6 0 0 1 5,2.2Z" fill="#fff"/></svg>P.O Box 218, Riverton Texas 75901</li>
    <li><svg viewBox="0 0 10 10" aria-hidden="true"><circle cx="5" cy="5" r="5" fill="var(--royal)"/><rect x="2.8" y="3.3" width="4.4" height="3.4" fill="#fff"/><path d="M2.8,3.3L5,5.2L7.2,3.3" fill="none" stroke="var(--royal)" stroke-width=".5"/></svg>office@northlinefoam.com</li>
    <li><svg viewBox="0 0 10 10" aria-hidden="true"><circle cx="5" cy="5" r="5" fill="var(--royal)"/><path d="M3.2,2.6L4.2,2.6L4.6,3.9L4,4.4C4.4,5.2 4.8,5.6 5.6,6L6.1,5.4L7.4,5.8L7.4,6.8C5,7.2 2.8,5 3.2,2.6Z" fill="#fff"/></svg>555-014-2290</li>
  </ul>
  <span class="folio">6</span>
</section>

</body>
</html>
```